Email Signature Block Design for Law Firm

I would like you to create a similar signature block for my law firm . I saw the email signature block attached as image002.png and wanted a similar design for my law firm. I want to be able to swap the portraits for each of my staff from the final design. Our law firm colors are black, gold, white, red.

Law

• i like the red circle in around the photo in the oak ridge guild design. The Tall Cedar Guild desgn is what inspired me to have a signature block design for my firm.

```html
<!DOCTYPE html>
<html lang="en">
<head>
<meta charset="UTF-8">
<title>Email Signature – The Harlow Firm</title>
<link href="https://fonts.googleapis.com/css2?family=Crimson+Pro:wght@500;700&family=Poppins:wght@400;500&family=Montserrat:wght@600;800&display=swap" rel="stylesheet">
<style>
  :root {
    --backdrop: #c2c2c2;
    --black-top: #1f1f1f;
    --black-bottom: #020202;
    --gold: #d8952b;
    --gold-light: #eeb04a;
    --red: #c3161f;
    --red-light: #e0313a;
    --red-deep: #8e0c13;
    --white: #ffffff;
    --ink: #0b0b0b;
  }
  * { margin: 0; padding: 0; box-sizing: border-box; }
  html, body {
    width: 1200px; height: 366px; overflow: hidden;
    background: var(--backdrop);
  }
  .signature {
    position: absolute; left: 91px; top: 65px;
    width: 1018px; height: 235px;
    background: linear-gradient(180deg, var(--black-top) 0%, #0e0e0e 45%, var(--black-bottom) 78%);
    box-shadow: 0 6px 6px rgba(0,0,0,0.35);
    overflow: hidden;
  }
  .gold-band {
    position: absolute; left: 0; bottom: 0;
    width: 100%; height: 53px; background: var(--gold);
    border-top: 3px solid var(--red);
  }
  .firm-mark {
    position: absolute; left: 22px; top: 24px;
    display: flex; align-items: center; gap: 12px;
  }
  .firm-mark .mark-square {
    width: 50px; height: 50px; background: var(--gold);
  }
  .firm-name {
    font-family: "Crimson Pro", serif; font-weight: 500;
    font-size: 24px; color: var(--white); letter-spacing: 0.6px;
    font-variant: small-caps; line-height: 1;
  }
  .firm-tagline {
    display: flex; align-items: center; gap: 5px; margin-top: 6px;
    font-family: "Montserrat", sans-serif; font-weight: 600;
    font-size: 8px; letter-spacing: 5.4px; color: var(--white);
    white-space: nowrap;
  }
  .firm-tagline::before, .firm-tagline::after {
    content: ""; width: 28px; height: 1px; background: var(--white);
  }
  .person-name {
    position: absolute; left: 21px; top: 102px;
    font-family: "Crimson Pro", serif; font-weight: 700;
    font-size: 40px; color: var(--white); letter-spacing: -0.3px; line-height: 1;
    white-space: nowrap;
  }
  .person-title {
    position: absolute; left: 22px; top: 134px;
    font-family: "Poppins", sans-serif; font-weight: 500;
    font-size: 18px; color: var(--white); line-height: 1;
  }
  .follow {
    position: absolute; left: 19px; top: 192px;
    display: flex; align-items: center;
  }
  .follow-label {
    font-family: "Montserrat", sans-serif; font-weight: 600;
    font-size: 13px; letter-spacing: 3.6px; color: var(--white);
    width: 173px; white-space: nowrap;
  }
  .social-list { display: flex; gap: 15px; list-style: none; }
  .social-list li {
    width: 16px; height: 16px; border-radius: 50%; background: var(--ink);
  }
  .portrait-ring {
    position: absolute; left: 416px; top: 25px;
    width: 186px; height: 186px; border-radius: 50%;
    background: radial-gradient(circle at 35% 30%, var(--red-light), var(--red) 55%, var(--red-deep));
    border: 3px solid var(--ink);
    display: flex; align-items: center; justify-content: center;
  }
  .portrait {
    width: 162px; height: 162px; border-radius: 50%;
    background: radial-gradient(circle at 50% 40%, #3a3a3a 0%, #1a1a1a 55%, #070707 100%);
  }
  .contact-list {
    position: absolute; left: 651px; top: 60px; list-style: none;
    font-family: "Poppins", sans-serif; font-weight: 400;
    font-size: 17px; color: var(--white); line-height: 18px;
  }
  .contact-list li { display: flex; align-items: flex-start; gap: 15px; }
  .contact-list li + li { margin-top: 14px; }
  .contact-icon {
    flex: none; width: 20px; height: 20px; border-radius: 50%;
    background: var(--gold); display: flex; align-items: center; justify-content: center;
  }
  .contact-icon svg { width: 12px; height: 12px; }
  .website {
    position: absolute; right: 25px; top: 186px;
    font-family: "Montserrat", sans-serif; font-weight: 800;
    font-size: 22px; letter-spacing: 4.2px; color: var(--white);
    white-space: nowrap;
  }
</style>
</head>
<body>
  <div class="signature">
    <div class="gold-band"></div>

    <div class="firm-mark">
      <span class="mark-square"></span>
      <div>
        <div class="firm-name">The Harlow Firm, pllc</div>
        <div class="firm-tagline">Attorneys At Law</div>
      </div>
    </div>

    <h1 class="person-name">MARCUS D. HARLOW</h1>
    <p class="person-title">Personal Injury Lawyer</p>

    <div class="follow">
      <span class="follow-label">FOLLOW US ON</span>
      <ul class="social-list" aria-label="Social profiles">
        <li></li><li></li><li></li><li></li><li></li>
      </ul>
    </div>

    <div class="portrait-ring">
      <div class="portrait" role="img" aria-label="Portrait photo of the attorney in a dark suit"></div>
    </div>

    <ul class="contact-list">
      <li>
        <span class="contact-icon">
          <svg viewBox="0 0 24 24"><path fill="#0b0b0b" d="M6.6 10.8a15.1 15.1 0 0 0 6.6 6.6l2.2-2.2a1 1 0 0 1 1-.25 11.4 11.4 0 0 0 3.6.57 1 1 0 0 1 1 1V20a1 1 0 0 1-1 1A17 17 0 0 1 3 4a1 1 0 0 1 1-1h3.5a1 1 0 0 1 1 1c0 1.25.2 2.45.57 3.57a1 1 0 0 1-.25 1z"/></svg>
        </span>
        <span>555-014-2730</span>
      </li>
      <li>
        <span class="contact-icon">
          <svg viewBox="0 0 24 24"><path fill="#0b0b0b" d="M12 2a7 7 0 0 0-7 7c0 5.2 7 13 7 13s7-7.8 7-13a7 7 0 0 0-7-7zm0 9.5A2.5 2.5 0 1 1 12 6.5a2.5 2.5 0 0 1 0 5z"/></svg>
        </span>
        <span>412 N Bayview Ave. Suite 118<br>Harbor City, FL 30419</span>
      </li>
      <li>
        <span class="contact-icon">
          <svg viewBox="0 0 24 24"><rect x="3" y="5" width="18" height="14" rx="1.5" fill="none" stroke="#0b0b0b" stroke-width="2"/><path d="M3.5 6l8.5 7 8.5-7" fill="none" stroke="#0b0b0b" stroke-width="2"/></svg>
        </span>
        <span>info@harlowfirm.com</span>
      </li>
    </ul>

    <div class="website">www.harlowfirm.com</div>
  </div>
</body>
</html>
```